Stationary (Letterhead, Business Card) for Varendo

Develop a unique and creative design for Letterhead and Business Cards for Varendo. Varendo will be a website with tips and tricks for amateur and professional photographers. The following Layouts have to be delivered:
1. Stationary/Letterhead A4 First Page
2. Business Card (Front- and back page) 85mm x 54mm

The design should be fresh and modern.

Font: Cabin (It's a open source Google font: [url removed, login to view])

Orange: HKS 8 (CMYK: 0/50/100/0)
Grey: CMYK 0/0/0/40
Black: CMYK 0/0/0/100

1. Letterhead A4 (First Page / Second Page): For easier use we want to have only the second page printed by a printer and will put all information from the first page in a word/pages-Layout. Please remember this if you design the letterhead. So please design a base for first and following pages which includes the logo, the name and possibly more elements which might be in color. All business information (like address etc.) can only be in black. The size is A4.

2. The business card is a double sided card in landscape format (85x54mm), no folding card, no rounded edges, no QR-code.
Frontpage: Some nice way to show the Logo and Name, derived from the original logo attached, probably on an orange background!
Backpage: Lot of white space, the Logo with the Company Name and the following information:

Varendo GmbH
Lindqvistweg 12
28391 Hallbergen

[url removed, login to view] (if not on front page)

Tobias Wendler (Name of the holder of the business card)
Geschäftsführender Gesellschafter (Job title)
+49 (3829) 52093716 (Telephone)
+49 (382) 6185 2049 (Mobile)
[url removed, login to view]@[url removed, login to view]

I added (German) print infos for both Letterhead and Business Cards.

Do you have any questions? Just ask :-) Looking forward to your ideas!

```html
<!DOCTYPE html>
<html lang="de">
<head>
<meta charset="utf-8">
<title>Varendo – Geschäftsausstattung</title>
<link rel="stylesheet" href="https://fonts.googleapis.com/css2?family=Cabin:wght@400;500;600;700&display=swap">
<style>
  :root {
    --orange: #f7941d;
    --orange-deep: #f28a12;
    --grey: #999b9e;
    --grey-text: #8a8c8e;
    --black: #1a1a1a;
    --frame: #9a9a9a;
    --paper: #ffffff;
    --tint: #f4f5f6;
  }
  * { margin: 0; padding: 0; box-sizing: border-box; }
  html, body { width: 1200px; height: 1121px; overflow: hidden; background: var(--paper); }
  body { font-family: "Cabin", sans-serif; color: var(--black); position: relative; }
  .abs { position: absolute; }

  .presentation-frame { position: absolute; left: 0; top: 0; width: 1200px; height: 1121px; border: 1px solid var(--frame); }

  /* Letterhead */
  .letterhead { left: 413px; top: 55px; width: 684px; height: 969px; border: 1px solid var(--frame); background: var(--paper); overflow: hidden; }
  .letterhead-tint { left: 0; top: 150px; width: 682px; height: 760px;
    background: radial-gradient(ellipse at 70% 45%, var(--tint) 0%, rgba(244,245,246,0.5) 45%, rgba(255,255,255,0) 75%); }
  .wordmark { display: flex; align-items: center; gap: 9px; font-weight: 500; }
  .wordmark-square { width: 16px; height: 16px; background: var(--orange); flex: none; }
  .letterhead .wordmark { left: 45px; top: 112px; font-size: 30px; color: var(--grey-text); }
  .sender { right: 48px; top: 40px; text-align: right; }
  .sender-company { font-size: 27px; font-weight: 500; line-height: 1; margin-bottom: 9px; }
  .sender-line { font-size: 9.5px; line-height: 12px; }
  .sender-person { font-size: 11.5px; font-weight: 700; margin-top: 12px; line-height: 14px; }
  .footer-info { right: 48px; bottom: 20px; text-align: right; font-size: 9.5px; line-height: 11.8px; }
  .footer-info .gap { height: 9px; }
  .footer-web { color: var(--orange); font-size: 14px; line-height: 16px; margin-top: 2px; }
  .letterhead-accent { left: 0; bottom: 0; width: 318px; height: 73px;
    background: linear-gradient(90deg, var(--orange) 0%, var(--orange) 40%, rgba(247,148,29,0.35) 80%, rgba(247,148,29,0) 100%); }

  /* Business card – contact side */
  .card { width: 287px; height: 187px; border: 1px solid #b5b5b5; overflow: hidden; }
  .card-contact { left: 76px; top: 355px; background: var(--paper); }
  .card-contact .band { left: 0; top: 0; }
  .card-contact .wordmark { left: 10px; top: 52px; font-size: 20px; color: var(--grey-text); gap: 6px; }
  .card-contact .wordmark-square { width: 11px; height: 11px; }
  .card-accent { right: 0; top: 12px; width: 44px; height: 72px;
    background: linear-gradient(180deg, rgba(247,148,29,0) 0%, rgba(247,148,29,0.5) 50%, var(--orange) 100%); }
  .holder { left: 22px; top: 105px; color: #fff; }
  .holder-name { font-size: 10.5px; font-weight: 700; line-height: 12px; }
  .holder-title { font-size: 8.5px; line-height: 11px; }
  .contact { left: 164px; top: 122px; color: #fff; font-size: 6.2px; line-height: 9.2px; }
  .contact-company { font-size: 8.5px; font-weight: 500; line-height: 10px; }
  .contact b { font-weight: 700; }

  /* Business card – brand side */
  .card-brand { left: 76px; top: 588px; background: var(--orange); border-color: var(--orange); }
  .card-brand .wordmark { left: 0; right: 0; top: 72px; justify-content: center; font-size: 28px; color: #fff; }
  .card-brand .wordmark-square { background: #fff; width: 14px; height: 14px; }
  .card-web { right: 8px; bottom: 6px; color: #fff; font-size: 11px; }
</style>
</head>
<body>
  <div class="presentation-frame"></div>

  <section class="abs letterhead" aria-label="Briefbogen">
    <div class="abs letterhead-tint" role="img" aria-label="Dezentes hellgraues Quadratmuster im Hintergrund"></div>
    <div class="abs wordmark"><span class="wordmark-square"></span>Varendo</div>
    <div class="abs sender">
      <div class="sender-company">Varendo GmbH</div>
      <div class="sender-line">Lindqvistweg 12</div>
      <div class="sender-line">28391 Hallbergen</div>
      <div class="sender-person">LUKAS VARNHOLT</div>
      <div class="sender-line">E-Mail: tobias.wendler@varendo.com</div>
      <div class="sender-line">Telephone: +49 (3829) 52093716</div>
    </div>
    <div class="abs footer-info">
      <div>Nordhafen Bank AG</div>
      <div>Konto: 5209 3716 0</div>
      <div>BLZ: 382 618 20</div>
      <div>IBAN: DE13 3829 5209 3716 2049 00</div>
      <div>BIC: NHBADEFFXXX</div>
      <div class="gap"></div>
      <div>Geschäftsführer: Tobias Wendler</div>
      <div>Amtsgericht Hallbergen HRB 3829 5209</div>
      <div>UStIdNr: DE382952093</div>
      <div class="footer-web">www.varendo.com</div>
    </div>
    <div class="abs letterhead-accent" role="img" aria-label="Orangefarbenes Pixelmuster am unteren Rand"></div>
  </section>

  <section class="abs card card-contact" aria-label="Visitenkarte Rückseite">
    <svg class="abs band" width="287" height="187" viewBox="0 0 287 187" aria-hidden="true">
      <polygon points="0,101 287,73 287,187 0,187" fill="var(--orange)"/>
    </svg>
    <div class="abs card-accent" role="img" aria-label="Orangefarbenes Pixelmuster"></div>
    <div class="abs wordmark"><span class="wordmark-square"></span>Varendo</div>
    <div class="abs holder">
      <div class="holder-name">TOBIAS WENDLER</div>
      <div class="holder-title">Geschäftsführender</div>
    </div>
    <div class="abs contact">
      <div class="contact-company">Varendo GmbH</div>
      <div>Lindqvistweg 12</div>
      <div>28391 Hallbergen</div>
      <div><b>T</b> +49 (3829) 52093716 (Telephone)</div>
      <div><b>M</b> +49 (382) 6185 2049 (Mobile)</div>
      <div><b>E</b> tobias.wendler@varendo.com</div>
    </div>
  </section>

  <section class="abs card card-brand" aria-label="Visitenkarte Vorderseite">
    <div class="abs wordmark"><span class="wordmark-square"></span>Varendo</div>
    <div class="abs card-web">www.varendo.com</div>
  </section>
</body>
</html>
```